e-Book Cover Design Project

I need an e-book cover design for a book called The Quiet Orchard. A handbook for hearts (turned sour). It is non-fiction. It has an apple theme throughout so I would like to see designs that use a red apple (perhaps even a bite out of it), simple text and simple background. Despite the theme, the final design should still be positive.

Target Market(s)

Most likely women aged 25 and over.

Requirements
Must have
• real red apple
Nice to have
• cupids arrow
Should not have
• cartoons

```html
<!DOCTYPE html>
<html lang="en">
<head>
<meta charset="utf-8">
<title>The Quiet Orchard – Cover</title>
<link rel="stylesheet" href="https://fonts.googleapis.com/css2?family=Macondo&family=Short+Stack&display=swap">
<style>
  :root {
    --cover-red: #e81f27;
    --paper: #fcfaf9;
    --blush: #fbd0c4;
    --ink: #111111;
    --apple-deep: #7e0d12;
    --apple-mid: #b3151c;
    --apple-light: #d8363b;
  }
  * { margin: 0; padding: 0; box-sizing: border-box; }
  html, body {
    width: 1200px;
    height: 849px;
    overflow: hidden;
    background: #ffffff;
  }
  .spread {
    position: relative;
    width: 1200px;
    height: 849px;
  }
  .front-cover {
    position: absolute;
    left: 0;
    top: 0;
    width: 596px;
    height: 849px;
    background: var(--paper);
  }
  .front-cover__art {
    position: absolute;
    inset: 0;
  }
  .title-kicker {
    font-family: "Short Stack", "Comic Neue", cursive;
    font-size: 34px;
    fill: var(--paper);
  }
  .title-main {
    font-family: "Macondo", "Georgia", serif;
    font-size: 150px;
  }
  .title-main--on-red { fill: var(--paper); }
  .title-main--on-paper { fill: var(--cover-red); }
  .author-name {
    font-family: "Short Stack", "Comic Neue", cursive;
    font-size: 29px;
    fill: var(--ink);
  }
  .cover-photo {
    position: absolute;
    left: 145px;
    top: 380px;
    width: 328px;
    height: 327px;
    background: radial-gradient(circle 145px at 180px 180px, var(--apple-light) 0%, var(--apple-mid) 55%, var(--apple-deep) 99%, transparent 100%);
  }
  .back-panel {
    position: absolute;
    left: 607px;
    top: 0;
    width: 593px;
    height: 849px;
    background: var(--paper);
  }
  .back-panel__tint {
    width: 100%;
    height: 597px;
    background: var(--blush);
  }
</style>
</head>
<body>
  <main class="spread">
    <section class="front-cover">
      <svg class="front-cover__art" width="596" height="849" viewBox="0 0 596 849" xmlns="http://www.w3.org/2000/svg">
        <defs>
          <clipPath id="upper-band">
            <rect x="0" y="0" width="596" height="238"/>
          </clipPath>
          <clipPath id="lower-field">
            <rect x="0" y="238" width="596" height="611"/>
          </clipPath>
        </defs>
        <rect class="header-band" x="0" y="0" width="596" height="238" fill="var(--cover-red)"/>
        <rect class="footer-bar" x="0" y="817" width="596" height="24" fill="var(--cover-red)"/>
        <text class="title-kicker" x="67" y="124" textLength="184" lengthAdjust="spacingAndGlyphs">The Quiet</text>
        <g class="title-main">
          <text class="title-main--on-red" x="65" y="290" textLength="425" lengthAdjust="spacingAndGlyphs" clip-path="url(#upper-band)">Orchard</text>
          <text class="title-main--on-paper" x="65" y="290" textLength="425" lengthAdjust="spacingAndGlyphs" clip-path="url(#lower-field)">Orchard</text>
        </g>
        <text class="author-name" x="231" y="792" textLength="195" lengthAdjust="spacingAndGlyphs">Author Name</text>
      </svg>
      <div class="cover-photo" role="img" aria-label="Photograph of a glossy red apple with a green leaf and a bite taken out of its side"></div>
    </section>
    <section class="back-panel">
      <div class="back-panel__tint"></div>
    </section>
  </main>
</body>
</html>
```